Amber Fen Racquet Club (Tennis Country Club)

Racquet and Tennis Country Club in Florida.
This web sight is needed for a Privet Tennis club located in Deerfield Beach city in Florida, USA.
We have 10 clay tennis courts and 2 hard tennis courts, small and cozy swimming pool and a clubhouse (see attached pictures) Attached pictures are for information only because we are under a reconstruction.
Updates

Target Market(s)

Adult members, Kids members, Tennis players

Coding

Coded - Design and coding required

Number of Pages Required

3 page

Requirements
Must have
• Logo colors (see attached file)

```html
<!DOCTYPE html>
<html lang="en">
<head>
<meta charset="utf-8">
<title>Amber Fen Racquet Club</title>
<link href="https://fonts.googleapis.com/css2?family=Lato:wght@400;700;900&display=swap" rel="stylesheet">
<style>
:root{
  --green:#17663a;
  --green-dark:#0f5530;
  --ink:#333333;
  --muted:#555555;
  --footer:#3b3b3b;
  --footer-text:#e6e6e6;
  --white:#ffffff;
  --btn-dark:#3a3a3a;
}
*{margin:0;padding:0;box-sizing:border-box}
html,body{width:1200px;height:2812px;overflow:hidden}
body{font-family:'Lato',sans-serif;color:var(--ink);background:var(--white);position:relative}
.abs{position:absolute}
.center{left:0;width:1200px;text-align:center}

/* hero */
.hero-photo{left:0;top:0;width:1200px;height:620px;background:linear-gradient(180deg,#4f5e72 0%,#6b7784 35%,#3d5a62 60%,#2b4a66 100%)}
.hero-shade{left:0;top:0;width:1200px;height:620px;background:rgba(20,30,40,.35)}
.brand{left:60px;top:0;width:180px;height:122px;background:var(--white);border-radius:0 0 22px 22px;display:flex;flex-direction:column;align-items:center;justify-content:center;gap:8px}
.brand-dot{width:46px;height:46px;border-radius:50%;background:var(--green)}
.brand-name{font-weight:700;font-size:26px;color:var(--ink)}
.nav{right:75px;top:22px;display:flex;gap:6px}
.nav a{display:block;color:var(--white);text-decoration:none;font-weight:700;font-size:13px;padding:12px 12px}
.nav a.active,.nav a.cta{background:var(--green);border-radius:3px}
.hero-title{top:236px;font-size:46px;font-weight:900;color:var(--white);letter-spacing:1px}
.hero-text{left:320px;width:560px;top:318px;font-size:13px;line-height:28px;color:var(--white);text-align:center}
.btn-green{background:var(--green);color:var(--white);font-weight:700;font-size:16px;display:flex;align-items:center;justify-content:center;border-radius:3px}
.hero-btn{left:528px;top:414px;width:144px;height:40px}
.dots{left:565px;top:508px;display:flex;gap:10px}
.dots span{width:11px;height:11px;border-radius:50%;background:var(--white)}
.dots span.on{background:var(--green)}
.wave{left:0;top:540px;width:1200px;height:200px}
.promo-text{left:138px;top:658px;font-size:18px;font-weight:700;color:var(--white);letter-spacing:.3px}
.btn-outline{border:2px solid var(--white);color:var(--white);font-weight:700;font-size:16px;display:flex;align-items:center;justify-content:center;border-radius:3px}
.promo-btn{left:918px;top:650px;width:144px;height:40px}

/* sections */
.section-title{font-size:31px;font-weight:900;color:var(--ink)}
.section-text{left:160px;width:880px;font-size:13.5px;line-height:28px;color:var(--muted);text-align:center}
.card{width:330px}
.card-photo{width:330px;height:180px}
.card-title{margin-top:20px;font-size:18px;font-weight:700}
.card-text{margin-top:12px;font-size:13.5px;line-height:24px;color:var(--muted)}
.btn-dark{margin-top:16px;width:92px;height:30px;background:var(--btn-dark);color:var(--white);font-size:12px;font-weight:700;display:flex;align-items:center;justify-content:center;border-radius:3px}

.join{left:0;top:1312px;width:1200px;height:345px;background:linear-gradient(180deg,#1e6d42,#155c36)}
.join-title{top:1396px;color:var(--white)}
.join-text{top:1446px;color:#e8f2ec}
.join-btn{left:529px;top:1530px;width:142px;height:38px;font-size:15px}

.tile{display:flex;align-items:center;justify-content:center;text-align:center;color:var(--white);font-size:28px;font-weight:700;line-height:28px}

/* footer */
.footer{left:0;top:2297px;width:1200px;height:515px;background:var(--footer)}
.footer-badge{left:559px;top:2256px;width:82px;height:82px;border-radius:50%;background:var(--footer);border:4px solid var(--white)}
.sub-title{top:2350px;font-size:28px;font-weight:700;color:var(--white)}
.sub-box{left:375px;top:2407px;width:450px;height:51px;background:var(--white);border-radius:4px}
.sub-box .ph{position:absolute;left:20px;top:17px;font-size:14px;color:#444}
.sub-box .go{position:absolute;right:10px;top:9px;width:122px;height:34px;background:var(--green-dark);color:var(--white);font-size:11px;font-weight:900;display:flex;align-items:center;justify-content:center;border-radius:3px}
.col-title{top:2518px;font-size:19px;font-weight:700;color:var(--white)}
.col-list{top:2564px;list-style:none;font-size:13.5px;color:var(--footer-text)}
.col-list li{height:33.5px}
.contact-icon{width:34px;height:34px;border-radius:50%;background:var(--green);display:flex;align-items:center;justify-content:center}
.contact-item{font-size:13.5px;color:var(--footer-text)}
.copyright{left:75px;top:2767px;font-size:13px;color:var(--footer-text)}
.social{left:990px;top:2746px;display:flex;gap:9px}
</style>
</head>
<body>

<!-- hero -->
<div class="abs hero-photo" role="img" aria-label="Photo of the club's tennis courts under floodlights with a rainbow in the sky"></div>
<div class="abs hero-shade"></div>

<div class="abs brand"><span class="brand-dot"></span><span class="brand-name">Amber Fen</span></div>

<nav class="abs nav">
  <a class="active">HOME</a><a>ABOUT US</a><a>TENNIS COURT</a><a>GALLERY</a><a>NEWS</a><a class="cta">LOGIN / REGISTER</a>
</nav>

<h1 class="abs center hero-title">AMBER FEN</h1>
<p class="abs hero-text">Velit ridiculus mattis. Ut fermentum maecenas pellentesque suscipit id urna quam egestas. Luctus sed a eu at augue placerat volutpat feugiat. Et quis scelerisque. Eget rhoncus phasellus praesent sem non.</p>
<div class="abs btn-green hero-btn">Read more</div>
<div class="abs dots"><span class="on"></span><span></span><span></span><span></span></div>

<svg class="abs wave" viewBox="0 0 1200 200" preserveAspectRatio="none">
  <path d="M0 10 Q300 60 600 55 Q900 50 1200 0 L1200 200 L0 200 Z" fill="var(--green)"/>
</svg>
<div class="abs promo-text">TURPIS SIT SED IN RISUS PELLENTESQUE LACUS SED SAEPE MUS SED URNA</div>
<div class="abs btn-outline promo-btn">Read more</div>

<!-- welcome -->
<h2 class="abs center section-title" style="top:786px">WELCOME TO AMBER FEN</h2>
<p class="abs section-text" style="top:839px">Velit ridiculus mattis. Ut fermentum maecenas pellentesque suscipit id urna quam egestas. Luctus sed a eu at augue placerat volutpat feugiat. Et quis scelerisque. Eget rhoncus phasellus praesent sem non.</p>

<article class="abs card" style="left:75px;top:919px">
  <div class="card-photo" role="img" aria-label="Photo of a player hitting a forehand on an outdoor court" style="background:linear-gradient(180deg,#5fa3d6,#bcd4e4 60%,#3b8a5a)"></div>
  <h3 class="card-title">Tennis Training</h3>
  <p class="card-text">Lorem ipsum dolor consectetur adipiscing Fusce varius euismod lacus eget feugiat rorem ipsum dolor consectetur Fusce varius [...]</p>
  <div class="btn-dark">Read more</div>
</article>
<article class="abs card" style="left:435px;top:919px">
  <div class="card-photo" role="img" aria-label="Photo of a player serving on an indoor court" style="background:linear-gradient(180deg,#1d1d1f,#3a3a3a 60%,#5a5a55)"></div>
  <h3 class="card-title">Best Court</h3>
  <p class="card-text">Lorem ipsum dolor consectetur adipiscing Fusce varius euismod lacus eget feugiat rorem ipsum dolor consectetur Fusce varius [...]</p>
  <div class="btn-dark">Read more</div>
</article>
<article class="abs card" style="left:795px;top:919px">
  <div class="card-photo" role="img" aria-label="Photo of a group of smiling players holding racquets" style="background:linear-gradient(180deg,#7faa5a,#e9e4dc 70%,#d8d2c8)"></div>
  <h3 class="card-title">Best Team</h3>
  <p class="card-text">Lorem ipsum dolor consectetur adipiscing Fusce varius euismod lacus eget feugiat rorem ipsum dolor consectetur Fusce varius [...]</p>
  <div class="btn-dark">Read more</div>
</article>

<!-- join -->
<div class="abs join" role="img" aria-label="Green band over a mosaic of member portraits"></div>
<h2 class="abs center section-title join-title">JOIN AMBER FEN TENNIS CLUB</h2>
<p class="abs section-text join-text">Velit ridiculus mattis. Ut fermentum maecenas pellentesque suscipit id urna quam egestas. Luctus sed a eu at augue placerat volutpat feugiat. Et quis scelerisque. Eget rhoncus phasellus praesent sem non.</p>
<div class="abs btn-outline join-btn">Join Now</div>

<!-- gallery -->
<h2 class="abs center section-title" style="top:1701px">OUR GALLERY</h2>
<p class="abs section-text" style="top:1754px">Velit ridiculus mattis. Ut fermentum maecenas pellentesque suscipit id urna quam egestas. Luctus sed a eu at augue placerat volutpat feugiat. Et quis scelerisque. Eget rhoncus phasellus praesent sem non.</p>

<div class="abs tile" role="img" aria-label="Photo of the club swimming pool" style="left:75px;top:1843px;width:422px;height:384px;background:linear-gradient(180deg,#3c4a3c 0%,#6a7a80 35%,#2a6aa0 60%,#1c4f80 100%)">SWIMMING POOL</div>
<div class="abs tile" role="img" aria-label="Photo of the clubhouse at night" style="left:519px;top:1843px;width:270px;height:158px;background:linear-gradient(180deg,#1a1a1a,#2c2c2c)">CLUB HOUSE</div>
<div class="abs tile" role="img" aria-label="Photo of the hard-court building" style="left:519px;top:2027px;width:270px;height:200px;background:linear-gradient(180deg,#6d6d6d,#3e3e3e)">2 HARD<br>TENNIS COURTS</div>
<div class="abs tile" role="img" aria-label="Photo of the clay tennis courts under a rainbow" style="left:817px;top:1843px;width:308px;height:384px;background:linear-gradient(180deg,#4b6078 0%,#7d8894 40%,#2f5a78 70%,#3a4a40 100%)">TENNIS COURTS</div>

<!-- footer -->
<footer>
<div class="abs footer"></div>
<div class="abs footer-badge"></div>
<h2 class="abs center sub-title">SUBSCRIBE NEWSLETTER</h2>
<div class="abs sub-box"><span class="ph">Enter Email id</span><span class="go">SUBSCRIBE</span></div>

<h4 class="abs col-title" style="left:79px">LINKS</h4>
<ul class="abs col-list" style="left:79px"><li>Course Flyover</li><li>Tennis Courts</li><li>Private Events</li><li>Swimming Pool</li></ul>

<h4 class="abs col-title" style="left:311px">EVENTS</h4>
<ul class="abs col-list" style="left:311px"><li>Group Tennis Events</li><li>Scorecard</li><li>Play Events</li><li>Group Events</li></ul>

<h4 class="abs col-title" style="left:542px">CONTACT US</h4>
<div class="abs contact-icon" style="left:540px;top:2574px"><svg width="14" height="18" viewBox="0 0 14 18"><path d="M7 0C3 0 0 3 0 7c0 5 7 11 7 11s7-6 7-11c0-4-3-7-7-7z" fill="#fff"/><circle cx="7" cy="7" r="2.6" fill="var(--green)"/></svg></div>
<div class="abs contact-item" style="left:591px;top:2566px">ADDRESS</div>
<div class="abs contact-item" style="left:591px;top:2600px">Linden Row Harbor City</div>
<div class="abs contact-icon" style="left:540px;top:2642px"><svg width="16" height="16" viewBox="0 0 16 16"><path d="M3 1l3 3-2 2c1 2 3 4 6 6l2-2 3 3-2 2C7 15 1 9 1 3z" fill="#fff"/></svg></div>
<div class="abs contact-item" style="left:591px;top:2634px">PHONE</div>
<div class="abs contact-item" style="left:591px;top:2668px">0800-555010 (24/7 Support Line)</div>
<div class="abs contact-icon" style="left:540px;top:2708px"><svg width="16" height="16" viewBox="0 0 16 16"><rect x="1" y="5" width="14" height="10" rx="1" fill="#fff"/><rect x="4" y="1" width="8" height="5" fill="#fff"/><rect x="4" y="8" width="8" height="1.5" fill="var(--green)"/><rect x="4" y="11" width="8" height="1.5" fill="var(--green)"/></svg></div>
<div class="abs contact-item" style="left:591px;top:2702px">FAX</div>
<div class="abs contact-item" style="left:591px;top:2736px">(555) 014-2277</div>

<h4 class="abs col-title" style="left:881px">QUICK LINKS</h4>
<ul class="abs col-list" style="left:883px"><li>Home</li><li>About Us</li><li>Tennis Courts</li><li>Gallery</li><li>Login / Register</li></ul>
<ul class="abs col-list" style="left:1035px"><li>FAQ</li><li>Testimonials</li><li>Sitemap</li></ul>

<div class="abs copyright">Copyright © 2018 . www.amberfen.example</div>
<div class="abs social">
  <svg width="40" height="44" viewBox="0 0 40 44"><polygon points="20,0 40,11 40,33 20,44 0,33 0,11" fill="#8a8a8a"/></svg>
  <svg width="40" height="44" viewBox="0 0 40 44"><polygon points="20,0 40,11 40,33 20,44 0,33 0,11" fill="#8a8a8a"/></svg>
  <svg width="40" height="44" viewBox="0 0 40 44"><polygon points="20,0 40,11 40,33 20,44 0,33 0,11" fill="#8a8a8a"/></svg>
</div>
</footer>

</body>
</html>
```